Business card for law firm

Need business card for new law firm. Think confident, authoritative, conservative, but not stuffy or old-fashioned.

Contact Information for Business Card

Content for card - logo (uploaded), plus the following:

Paul Wexbury (larger font)
Managing Partner (larger font, but not as large as name)
Level 9, 41 Tansy Lane
Sydney NSW 2000
Main Tel 02 7346 2190
Direct Tel 02 6273 4415
Email paul@qvlegal.com.au
www.qvlegal.com.au

Letterhead design should include logo plus:
Level 9, 41 Tansy Lane
Sydney NSW 2000
Tel 02 6273 4415
www.qvlegal.com.au

```html
<!DOCTYPE html>
<html lang="en">
<head>
<meta charset="utf-8">
<title>Quayvale Lawyers — Letterhead</title>
<link rel="stylesheet" href="https://fonts.googleapis.com/css2?family=Arimo:wght@400;700&display=swap">
<style>
  :root {
    --backdrop: #869a97;
    --paper: #ffffff;
    --navy: #0b0f6b;
    --ink: #111111;
    --rule: #3a3a52;
    --label: #ffffff;
  }
  * { margin: 0; padding: 0; box-sizing: border-box; }
  html, body {
    width: 1200px;
    height: 800px;
    overflow: hidden;
    background: var(--backdrop);
  }
  .canvas {
    position: relative;
    width: 1200px;
    height: 800px;
    background: var(--backdrop);
    font-family: "Arimo", Arial, sans-serif;
  }
  .sheet {
    position: absolute;
    top: 74px;
    width: 440px;
    height: 569px;
    background: var(--paper);
  }
  .sheet--mono { left: 79px; }
  .sheet--accent { left: 621px; }

  .sheet__edge-bar {
    position: absolute;
    left: 0;
    top: 30px;
    width: 7px;
    height: 55px;
    background: var(--navy);
  }
  .brand {
    position: absolute;
    left: 30px;
    top: 36px;
    width: 96px;
    text-align: center;
  }
  .brand__mark {
    display: block;
    width: 16px;
    height: 16px;
    margin: 0 auto 9px;
    background: var(--navy);
  }
  .brand__name {
    display: block;
    font-family: "Arimo", Arial, sans-serif;
    font-weight: 700;
    font-size: 10px;
    line-height: 1;
    color: var(--navy);
    white-space: nowrap;
  }

  .footer {
    position: absolute;
    left: 24px;
    top: 505px;
    width: 389px;
  }
  .footer__divider {
    display: block;
    width: 389px;
    height: 20px;
  }
  .footer__contact {
    margin-top: 1px;
    padding-left: 5px;
    font-size: 6.5px;
    line-height: 7.4px;
    color: var(--ink);
  }
  .footer__firm {
    font-weight: 700;
    font-size: 7.5px;
    line-height: 9px;
    letter-spacing: 0.2px;
  }
  .sheet--accent .footer__firm { color: var(--navy); }

  .caption {
    position: absolute;
    left: 0;
    top: 666px;
    width: 1200px;
    text-align: center;
    color: var(--label);
    font-family: "Arimo", Arial, sans-serif;
    font-weight: 400;
    font-size: 88px;
    line-height: 1;
    letter-spacing: 8px;
  }
</style>
</head>
<body>
<main class="canvas">

  <section class="sheet sheet--mono" aria-label="Letterhead, black footer">
    <div class="sheet__edge-bar"></div>
    <div class="brand">
      <span class="brand__mark"></span>
      <span class="brand__name">QUAYVALE LAWYERS</span>
    </div>
    <div class="footer">
      <svg class="footer__divider" viewBox="0 0 389 20" aria-hidden="true">
        <line x1="0" y1="10" x2="182" y2="10" stroke="var(--rule)" stroke-width="1"/>
        <rect x="187" y="3" width="14" height="14" fill="var(--navy)"/>
        <line x1="207" y1="10" x2="389" y2="10" stroke="var(--rule)" stroke-width="1"/>
      </svg>
      <div class="footer__contact">
        <p class="footer__firm">QUAYVALE LAWYERS</p>
        <p>Level 9, 41 Tansy Lane Sydney NSW 2000</p>
        <p>TEL: 02 7346 2190 , 02 6273 4415</p>
        <p>EMAIL: paul@qvlegal.com.au &nbsp;WEB: www.qvlegal.com.au</p>
      </div>
    </div>
  </section>

  <section class="sheet sheet--accent" aria-label="Letterhead, navy footer">
    <div class="sheet__edge-bar"></div>
    <div class="brand">
      <span class="brand__mark"></span>
      <span class="brand__name">QUAYVALE LAWYERS</span>
    </div>
    <div class="footer">
      <svg class="footer__divider" viewBox="0 0 389 20" aria-hidden="true">
        <line x1="0" y1="10" x2="182" y2="10" stroke="var(--rule)" stroke-width="1"/>
        <rect x="187" y="3" width="14" height="14" fill="var(--navy)"/>
        <line x1="207" y1="10" x2="389" y2="10" stroke="var(--rule)" stroke-width="1"/>
      </svg>
      <div class="footer__contact">
        <p class="footer__firm">QUAYVALE LAWYERS</p>
        <p>Level 9, 41 Tansy Lane Sydney NSW 2000</p>
        <p>TEL: 02 7346 2190 , 02 6273 4415</p>
        <p>EMAIL: paul@qvlegal.com.au &nbsp;WEB: www.qvlegal.com.au</p>
      </div>
    </div>
  </section>

  <h1 class="caption">LETTERHEAD</h1>

</main>
</body>
</html>
```